Brightwell Cleaning Services - Redesign

I've got my website designed a few years ago and it looks dated now. I would like to get a modern, happy, bright, and clean look. All the content needed can be found at my current website www.brightwellhq.example. Not necessarily need to use all of it, since I want something more clean and easy to read.
I need a 5 pages website:
HOME | SERVICES | ESTIMATE |TESTIMONIALS | CONTACT US

Industry/Entity Type

Janitorial Service

Number of Pages Required

5+ page

Colors
0792cd
34a6d7
85cae6
cee9f5
ebebeb
f0f0f0
f5f5f5
b1b1b1
000000

Requirements
Must have
• Who we are?
• Brightwell Cleaning Services is a local, family-owned, client-focused house and office cleaning company that strives to ensure the highest level of customer satisfaction. We offer expert residential and commercial cleaning services to all the Seattle and Eastside areas.
• Why Brightwell?
• √ We are insured, bonded and licensed.
•  Brightwell Cleaning Service is Fully Insured so you can rest easy knowing your home is protected.
•  Copy of insurance available upon request.
•

√ We provide all supplies and equipments needed to thoroughly clean your home or business.

• √ We are not a franchise. We are a local, family-owned company.

• When you call Brightwell Cleaning Services, you’ll always speak to one of the owners, which is a great benefit to you since this allows us to give you the personal attention and more time needed to clean your home the way you want it cleaned.

• √ We are good at what we do, and we like doing it.

```html
<!DOCTYPE html>
<html lang="en">
<head>
<meta charset="utf-8">
<title>Brightwell Cleaning Services</title>
<link href="https://fonts.googleapis.com/css2?family=Montserrat:wght@400;500;600&family=Lato:ital,wght@0,400;0,700;1,400&display=swap" rel="stylesheet">
<style>
  :root {
    --blue-deep: #0792cd;
    --blue: #34a6d7;
    --blue-soft: #85cae6;
    --blue-pale: #cee9f5;
    --grey-1: #ebebeb;
    --grey-2: #f0f0f0;
    --grey-3: #f5f5f5;
    --grey-mid: #b1b1b1;
    --ink: #000000;
    --heading-grey: #c4c8cc;
    --navy: #1b5d8f;
    --white: #ffffff;
    --nav-text: #6f7479;
    --gold: #f2b642;
    --green: #8fd14f;
  }
  * { box-sizing: border-box; margin: 0; padding: 0; }
  html, body { width: 1200px; height: 2166px; overflow: hidden; }
  body { position: relative; background: var(--white); font-family: "Lato", Arial, sans-serif; color: var(--ink); }

  .site-nav { position: absolute; left: 0; top: 0; width: 1200px; height: 66px; background: var(--white); border-top: 3px solid var(--blue-pale); z-index: 3; }
  .site-nav a { position: absolute; top: 28px; font-family: "Montserrat", Arial, sans-serif; font-size: 11.5px; letter-spacing: 0.6px; color: var(--nav-text); text-decoration: none; white-space: nowrap; }
  .site-nav a.is-active { color: var(--gold); }
  .site-nav a.is-active::after { content: ""; position: absolute; left: 0; right: 0; top: 22px; height: 2px; background: var(--gold); }
  .site-nav a.nav-contact { color: var(--blue); }
  .site-nav .nav-call { color: var(--blue-soft); display: flex; align-items: center; gap: 4px; }

  .brand-tag { position: absolute; left: 566px; top: 69px; width: 113px; height: 55px; background: var(--white); z-index: 3; display: flex; align-items: center; justify-content: center; gap: 6px; }
  .brand-tag span { font-family: "Montserrat", Arial, sans-serif; font-weight: 600; font-size: 16px; color: var(--blue-deep); }
  .brand-tag i { width: 8px; height: 8px; background: var(--blue); border-radius: 50%; }

  .hero { position: absolute; left: 0; top: 66px; width: 1200px; height: 513px; }
  .hero-photo { position: absolute; inset: 0; background: linear-gradient(100deg, #5f8fb0 0%, #6f9cbf 30%, #8ab4d6 55%, #9cc3e1 75%, #b6d4ea 100%); }
  .hero-copy { position: absolute; left: 0; right: 0; top: 200px; text-align: center; color: var(--white); }
  .hero-copy h1 { font-family: "Montserrat", Arial, sans-serif; font-weight: 500; font-size: 26px; letter-spacing: 0.5px; }
  .hero-copy p { margin: 22px auto 0; width: 620px; font-size: 15px; line-height: 22px; }

  .section-title { position: absolute; left: 0; width: 1200px; text-align: center; font-family: "Montserrat", Arial, sans-serif; font-weight: 400; font-size: 21px; letter-spacing: 1px; color: var(--heading-grey); }

  .service { position: absolute; width: 470px; height: 124px; }
  .service-badge { position: absolute; left: 0; top: 0; width: 122px; height: 122px; border-radius: 50%; border: 3px solid var(--blue-deep); background: var(--grey-2); display: flex; align-items: center; justify-content: center; box-shadow: inset 0 0 0 6px var(--white); }
  .service-badge.is-soft { border-color: var(--blue); }
  .service h3 { position: absolute; left: 131px; top: 17px; font-family: "Montserrat", Arial, sans-serif; font-weight: 400; font-size: 20px; letter-spacing: 0.8px; color: var(--heading-grey); white-space: nowrap; }
  .service p { position: absolute; left: 134px; top: 56px; width: 270px; font-size: 12.5px; line-height: 21px; color: var(--grey-mid); }

  .testimonial-band { position: absolute; left: 0; top: 1103px; width: 1200px; height: 227px; background: linear-gradient(90deg, #c9c9c9 0%, #bcbcbc 40%, #d2d2d2 70%, #c4c4c4 100%); }
  .testimonial-band h2 { position: absolute; left: 143px; top: 33px; font-family: "Montserrat", Arial, sans-serif; font-weight: 500; font-size: 22px; letter-spacing: 1.5px; color: var(--navy); }
  .testimonial-band blockquote { position: absolute; left: 143px; top: 68px; width: 900px; font-style: italic; font-size: 15px; line-height: 24px; color: var(--white); }
  .btn-more { position: absolute; left: 143px; top: 153px; width: 149px; height: 37px; border-radius: 19px; background: var(--blue); color: var(--white); font-size: 14px; display: flex; align-items: center; justify-content: center; gap: 12px; text-decoration: none; }

  .category { position: absolute; width: 293px; height: 216px; }
  .category .play { position: absolute; left: 50%; top: 50%; width: 64px; height: 64px; margin: -32px 0 0 -32px; border-radius: 50%; background: rgba(255,255,255,0.35); border: 2px solid rgba(255,255,255,0.7); display: flex; align-items: center; justify-content: center; }

  .site-footer { position: absolute; left: 0; top: 1957px; width: 1200px; height: 182px; background: var(--grey-3); }
  .footer-links { position: absolute; left: 152px; top: 18px; list-style: none; }
  .footer-links li { font-size: 11.5px; line-height: 27.4px; color: #c6cacd; display: flex; align-items: center; gap: 11px; }
  .footer-links li::before { content: ""; width: 5px; height: 5px; border-radius: 50%; background: var(--blue-soft); }
  .gift-card { position: absolute; left: 348px; top: 68px; width: 267px; height: 60px; border: 2px solid var(--blue-deep); background: linear-gradient(90deg, var(--blue) 0%, var(--blue-soft) 50%, var(--blue) 100%); }
  .payment-label { position: absolute; left: 716px; top: 45px; font-size: 11.5px; color: #c6cacd; }
  .payment-cards { position: absolute; left: 713px; top: 69px; display: flex; gap: 5px; }
  .payment-cards span { width: 101px; height: 63px; border-radius: 5px; background: var(--white); border: 1px solid var(--grey-1); display: flex; align-items: center; justify-content: center; font-family: "Lato", Arial, sans-serif; font-weight: 700; font-size: 15px; color: var(--blue-deep); }

  .legal-bar { position: absolute; left: 0; top: 2139px; width: 1200px; height: 27px; background: var(--blue-soft); color: var(--white); font-size: 12px; }
  .legal-bar .rights { position: absolute; left: 284px; top: 6px; }
  .legal-bar .mail { position: absolute; right: 83px; top: 6px; }
</style>
</head>
<body>

<nav class="site-nav">
  <a class="is-active" style="left:169px" href="#">HOME</a>
  <a style="left:247px" href="#">SERVICE</a>
  <a style="left:332px" href="#">ESTIMATES</a>
  <a style="left:433px" href="#">TESTIMONIALS</a>
  <a style="left:559px" href="#">GIFT CERTIFICATES</a>
  <a style="left:726px" href="#">TESTIMONIALS</a>
  <a class="nav-contact" style="left:861px" href="#">CONTACT US</a>
  <a class="nav-call" style="left:982px" href="#">
    <svg width="12" height="12" viewBox="0 0 24 24"><path fill="#8fd14f" d="M6.6 10.8a15 15 0 0 0 6.6 6.6l2.2-2.2c.3-.3.7-.4 1-.2 1.1.4 2.3.6 3.6.6.6 0 1 .4 1 1V20c0 .6-.4 1-1 1A17 17 0 0 1 3 4c0-.6.4-1 1-1h3.5c.6 0 1 .4 1 1 0 1.3.2 2.5.6 3.6.1.3 0 .7-.2 1z"/></svg>
    CALL - 425-555-0142
  </a>
</nav>

<div class="brand-tag"><i></i><span>Brightwell</span></div>

<header class="hero">
  <div class="hero-photo" role="img" aria-label="Smiling businesswoman on the phone at a laptop in front of a green plant wall, tinted blue"></div>
  <div class="hero-copy">
    <h1>WHO WE ARE</h1>
    <p>A local, family-owned, client-focused house and office cleaning company serving all the Seattle and Eastside areas.</p>
  </div>
</header>

<h2 class="section-title" style="top:609px">WELCOME TO OUR SERVICES</h2>

<article class="service" style="left:160px; top:722px">
  <div class="service-badge">
    <svg width="54" height="54" viewBox="0 0 54 54" fill="#b9bcbf"><rect x="10" y="20" width="8" height="26"/><rect x="20" y="8" width="10" height="38"/><rect x="32" y="14" width="8" height="32"/><rect x="42" y="26" width="6" height="20"/><rect x="4" y="46" width="46" height="3"/></svg>
  </div>
  <h3>OFFICE CLEANING</h3>
  <p>Expert commercial cleaning for offices on a weekly, bi-weekly or monthly schedule.</p>
</article>

<article class="service" style="left:661px; top:722px">
  <div class="service-badge is-soft">
    <svg width="60" height="54" viewBox="0 0 60 54" fill="none" stroke="#b9bcbf" stroke-width="5" stroke-linejoin="round"><path d="M6 28 30 6l24 22"/><path d="M13 24v24h34V24"/><rect x="25" y="32" width="10" height="16" fill="#b9bcbf" stroke="none"/></svg>
  </div>
  <h3>RESIDENTIAL CLEANING</h3>
  <p>We also offer one time house cleaning for days when your schedule is too full.</p>
</article>

<article class="service" style="left:160px; top:939px">
  <div class="service-badge is-soft">
    <svg width="48" height="48" viewBox="0 0 48 48" fill="none" stroke="#b9bcbf" stroke-width="4" stroke-linecap="round"><path d="M6 6l36 36M42 6 6 42"/><path d="M6 16V6h10M32 6h10v10M42 32v10H32M16 42H6V32"/></svg>
  </div>
  <h3>MOVE OUT/ IN CLEANING</h3>
  <p>We are insured, bonded and licensed. Copy of insurance available upon request.</p>
</article>

<article class="service" style="left:661px; top:939px">
  <div class="service-badge">
    <svg width="58" height="46" viewBox="0 0 58 46" fill="#b9bcbf"><path d="M4 6c8-2 16-1 23 3v34c-7-4-15-5-23-3z"/><path d="M54 6c-8-2-16-1-23 3v34c7-4 15-5 23-3z"/></svg>
  </div>
  <h3 style="top:21px">SCHOOL/DAYCARE</h3>
  <p style="top:60px">We provide all supplies and equipment needed to clean your space thoroughly.</p>
</article>

<section class="testimonial-band" role="img" aria-label="Blurred photo of people shaking hands at a desk, in grey tones">
  <h2>TESTIMONIALS</h2>
  <blockquote>Brightwell is not a franchise, and it shows. Every time I call I speak to one of the owners, who listens and makes sure the house is cleaned exactly the way I want. They are good at what they do and clearly like doing it. Just wanted to take the time to thank you for the tremendous work you did at my parent's house.</blockquote>
  <a class="btn-more" href="#">Read More
    <svg width="12" height="12" viewBox="0 0 12 12" fill="none" stroke="#fff" stroke-width="2"><path d="M1 6h9M6 2l4 4-4 4"/></svg>
  </a>
</section>

<h2 class="section-title" style="top:1364px">OUR CATEGORIES</h2>

<div class="category" style="left:82px; top:1419px; background:linear-gradient(135deg,#d88a4a,#c99a64 50%,#e3b88a)" role="img" aria-label="Wooden desk with an orange chair and notebooks seen from above"><span class="play"><svg width="22" height="24" viewBox="0 0 22 24"><path d="M3 2l17 10L3 22z" fill="none" stroke="#fff" stroke-width="2.5"/></svg></span></div>
<div class="category" style="left:436px; top:1419px; background:linear-gradient(180deg,#1d2a3c,#3a4a5e 50%,#2f6a8a)" role="img" aria-label="Villa with a lit swimming pool at dusk"><span class="play"><svg width="22" height="24" viewBox="0 0 22 24"><path d="M3 2l17 10L3 22z" fill="none" stroke="#fff" stroke-width="2.5"/></svg></span></div>
<div class="category" style="left:790px; top:1419px; background:linear-gradient(135deg,#6a6a6a,#a9a9a9 50%,#d6d6d6)" role="img" aria-label="Black and white keyboard with a mug and a hand on a mouse"><span class="play"><svg width="22" height="24" viewBox="0 0 22 24"><path d="M3 2l17 10L3 22z" fill="none" stroke="#fff" stroke-width="2.5"/></svg></span></div>
<div class="category" style="left:82px; top:1692px; background:linear-gradient(135deg,#3fa9e6,#6cc0ef 50%,#4db0ea)" role="img" aria-label="Team of office workers cheering, tinted blue"><span class="play"><svg width="22" height="24" viewBox="0 0 22 24"><path d="M3 2l17 10L3 22z" fill="none" stroke="#fff" stroke-width="2.5"/></svg></span></div>
<div class="category" style="left:436px; top:1692px; background:linear-gradient(135deg,#4a4236,#8a7a62 50%,#d8cdbd)" role="img" aria-label="Computer monitor and keyboard on a wooden desk"><span class="play"><svg width="22" height="24" viewBox="0 0 22 24"><path d="M3 2l17 10L3 22z" fill="none" stroke="#fff" stroke-width="2.5"/></svg></span></div>
<div class="category" style="left:790px; top:1692px; background:linear-gradient(90deg,#e6e2dc 0%,#cfc9c1 47%,#3e5a82 53%,#1f2f4a 100%)" role="img" aria-label="Split view of a made bed with pillows and an office with black chairs"><span class="play"><svg width="22" height="24" viewBox="0 0 22 24"><path d="M3 2l17 10L3 22z" fill="none" stroke="#fff" stroke-width="2.5"/></svg></span></div>

<footer class="site-footer">
  <ul class="footer-links">
    <li>Home</li>
    <li>Service</li>
    <li>Estimates</li>
    <li>Testimonials</li>
    <li>Contact Us</li>
    <li>Gift Certificates</li>
  </ul>
  <div class="gift-card" role="img" aria-label="Gift certificate banner inviting visitors to order gift certificates"></div>
  <div class="payment-label">Payment Center</div>
  <div class="payment-cards">
    <span>Veyra</span>
    <span>Mintcard</span>
    <span>Amplex</span>
    <span>Roamer</span>
  </div>
</footer>

<div class="legal-bar">
  <span class="rights">2016 All Rights Reserved Brightwell Cleaning Services</span>
  <span class="mail">Email- info@brightwellhq.example</span>
</div>

</body>
</html>
```